Wordpress Design Project

Hi,

I would like a more modern colourful design doing for my website Zyl Pando (www.zy%lpando.com - remove percentage). But I do still want to keep the same sort of colors, just maybe lighter. More interesting.

I want the inside pages to NOT all look the same with just boring text.

I want the site to look more appealing and maybe a new logo.
Updates

I would like to mention I would prefer to keep the same logo after rethinking it (possibly a slight refresh of the logo if you feel its a good idea) and the same color scheme as at present.

Saves us rebranding a lot of our apps, tools online ads etc.

Also I thought it is worth mentioning we have 2 parts to the site. The front end and the logged in area. It would be good if when making the front end you keep in mind the back end at http://p.zy%lpando.com (remove percentage). We can only edit this limitedly (can edit the entire footer, the logo and full CSS of it). Would be good if we could make sure the header and footer can be used on the back end as well maybe to make it match.

I also want layouts making not just for the homepage. Obviously every page will basically be the same but I don't want all the other pages to just be 'text' and no real layout.

You can see out main pages on the website at the moment, I want those other pages to be laid out nice and differently as well. For example the testimonials page could be more interesting with speech bubbles and pictures of each person (just use placeholders). The affiliates page could be a description and then a nice fancy list of features why to join etc. 

Nothing overly complicated but I think it makes the whole site seem a lot better.

Target Market(s)

Affiliate Marketing. International.

Requirements
Must have
• Needs to be more room for links across the navigation at the top, also sub menus (at present we have a lot of pages which are hidden deep within other pages).
Nice to have
• Lists of features for advertisers and affiliates on the homepage part.

Menu items and buttons have nice hover over effects.

I want to get across on our pages all the different unique features we have.

Maybe some kind of slider which has past offer logos in, just use example logos.

```html
<!DOCTYPE html>
<html lang="en">
<head>
<meta charset="utf-8">
<title>Zyl Pando – International Affiliate Network</title>
<link href="https://fonts.googleapis.com/css2?family=Roboto+Condensed:wght@400;700&family=Open+Sans:wght@400;600;700&display=swap" rel="stylesheet">
<style>
:root{
  --orange:#f7941d;
  --orange-dark:#e57d0c;
  --blue:#0b5d9b;
  --blue-deep:#0a4f86;
  --blue-light:#5bb4e8;
  --teal:#1aa3bf;
  --yellow:#fcc92e;
  --band:#e5efef;
  --grey-text:#6d6d6d;
  --dark:#222;
  --panel:#f1f1f1;
  --line:#dcdcdc;
}
*{margin:0;padding:0;box-sizing:border-box}
html,body{width:796px;height:1200px;overflow:hidden;background:#fff}
body{position:relative;font-family:"Open Sans",Arial,sans-serif;color:var(--dark)}
.abs{position:absolute}

/* header */
.site-header{position:absolute;left:0;top:0;width:796px;height:68px}
.brand{left:113px;top:12px;font-family:"Roboto Condensed",sans-serif;font-weight:700;font-size:40px;color:var(--orange);line-height:44px;letter-spacing:-1px}
.pill{height:19px;border-radius:10px;background:linear-gradient(#2d8fd8,#0d62a8);color:#fff;font-family:"Roboto Condensed",sans-serif;font-size:10.5px;line-height:19px;text-align:center;box-shadow:0 1px 0 #0a4f86}
.phone{right:100px;top:40px;font-size:15.5px;font-weight:700;color:#111}

/* nav */
.main-nav{left:0;top:68px;width:796px;height:25px;background:linear-gradient(#f9a633,#ee8410);border-top:1px solid #fbb64d}
.main-nav ul{list-style:none;display:flex;position:absolute;left:117px;top:0;height:25px}
.main-nav li{font-family:"Roboto Condensed",sans-serif;font-size:13.5px;color:#fff;line-height:25px;padding:0 9px}
.main-nav li.active{background:var(--blue);padding:0 5px}

/* hero */
.hero{left:0;top:93px;width:796px;height:349px;background:radial-gradient(ellipse at 45% 40%,#1476b9,#0a5592 75%)}
.hero-title{left:0;width:796px;text-align:center;color:#fff;font-family:"Roboto Condensed",sans-serif;font-weight:700;top:102px;font-size:20px;line-height:22px}
.hero-title span{display:block;font-size:31px;line-height:34px}
.map{left:150px;top:155px;width:480px;height:210px;border-radius:40% 45% 35% 40%;background:radial-gradient(ellipse,#74c6f1,#4fa6de 70%,rgba(79,166,222,0) 72%)}
.laptop{left:90px;top:280px;width:185px;height:162px;background:linear-gradient(160deg,#d9e04a,#a2b121 55%,#c7c7c7 80%);border-radius:8px 8px 2px 2px;opacity:.9}
.feature-list{left:637px;top:128px;width:90px;list-style:none;color:#fff;font-family:"Roboto Condensed",sans-serif;font-weight:700;font-size:10px;line-height:10px}
.feature-list li{height:62px}
.feature-list svg{display:block;margin-bottom:3px}
.join-btn{left:392px;top:392px;width:129px;height:28px;border-radius:14px;background:linear-gradient(#f7942a,#e0580d);border:2px solid #fff;color:#fff;font-family:"Roboto Condensed",sans-serif;font-weight:700;font-size:14px;line-height:24px;text-align:center;box-shadow:0 2px 3px rgba(0,0,0,.35)}
.dots{left:639px;top:428px;display:flex;gap:4px}
.dots i{width:7px;height:7px;border-radius:50%;background:#fff}
.dots i:first-child{background:var(--orange)}

/* intro band */
.intro{left:0;top:442px;width:796px;height:143px;background:var(--band)}
.intro-hatch{left:0;top:576px;width:796px;height:9px;background:repeating-linear-gradient(45deg,#d5dfdf 0 1px,transparent 1px 4px)}
.intro-col{top:452px;width:292px}
.intro-col h2{font-family:"Roboto Condensed",sans-serif;font-weight:700;font-size:19px;color:var(--orange);margin-bottom:7px}
.intro-col p{font-size:9.4px;line-height:14.5px;color:#555}
.cta{top:534px;width:115px;height:29px;border-radius:4px;background:linear-gradient(#fed74a,#f4b212);border-bottom:2px solid #d99a0b;font-family:"Roboto Condensed",sans-serif;font-weight:700;font-size:15px;line-height:27px;text-align:center;color:#333}

/* sidebar */
.login-box{left:99px;top:600px;width:142px;height:164px;background:var(--panel);border-radius:4px}
.side-h{font-family:"Roboto Condensed",sans-serif;font-size:14px;color:#111}
.field{left:113px;width:115px;height:25px;background:#fff;border-radius:3px;font-size:9.5px;padding:6px 6px;color:#222}
.small{font-size:8.5px;color:#333}
.login-btn{left:112px;top:730px;width:44px;height:21px;border-radius:4px;border:1px solid #aaa;background:linear-gradient(#fff,#ddd);font-size:9.5px;font-weight:600;text-align:center;line-height:19px}
.post-list{left:99px;top:805px;width:142px;list-style:none}
.post-list li{font-size:8.5px;color:#777;height:19px;line-height:19px;border-bottom:1px solid #e8e8e8;padding-left:8px;position:relative}
.post-list li::before{content:"›";position:absolute;left:0;color:#999}
.social{top:907px;width:26px;height:26px;border-radius:3px}

/* welcome */
.welcome-h{left:266px;top:598px;font-family:"Roboto Condensed",sans-serif;font-size:20px;color:var(--teal)}
.welcome{left:266px;top:629px;width:432px}
.welcome p{font-size:8.7px;line-height:12.6px;color:#777;margin-bottom:6.5px}

.why{left:267px;top:788px;width:202px;height:149px;background:var(--orange);border-radius:4px;color:#fff;padding:9px 12px}
.why h3{font-family:"Roboto Condensed",sans-serif;font-weight:400;font-size:14.5px;margin-bottom:9px}
.why ul{list-style:none}
.why li{font-size:8.6px;line-height:15.5px}
.why li::before{content:"› "}
.why li.wrap{line-height:11px;margin:2px 0 3px}
.testi-h{left:496px;top:795px;font-family:"Roboto Condensed",sans-serif;font-size:14.5px;color:var(--teal)}
.testi{left:496px;top:819px;width:200px;font-size:8.6px;line-height:14.8px;color:#666}
.testi-rule{left:496px;top:927px;width:200px;height:1px;background:#d5d5d5}
.testi-by{left:589px;top:936px;font-size:9px;color:#222}

/* advertisers */
.adv-h{left:0;top:976px;width:796px;text-align:center;font-family:"Roboto Condensed",sans-serif;font-size:14px;color:var(--blue)}
.rule{left:99px;width:598px;height:1px;background:#e2e2e2}
.adv-logo{top:1008px;width:70px;text-align:center;font-size:9px;color:#222}
.adv-logo i{display:block;margin:0 auto 4px;width:40px;height:40px}
.badge{top:1105px;width:88px;height:25px;border:1px solid #cfd8dc;background:#f7f9fa;display:flex;align-items:center;gap:5px;padding:0 5px}
.badge i{width:16px;height:16px;border-radius:3px;flex:none}
.badge b{display:block;font-size:6.5px;color:#1b5d94;line-height:8px}
.badge s{display:block;text-decoration:none;font-size:4.5px;color:#777;line-height:6px}

/* footer */
.site-footer{left:0;top:1143px;width:796px;height:57px;background:#e8eeee}
.footer-hatch{left:0;top:1143px;width:796px;height:9px;background:repeating-linear-gradient(45deg,#d4dcdc 0 1px,transparent 1px 4px)}
.foot-links{left:0;top:1160px;width:796px;display:flex;justify-content:center;font-size:8.5px;color:#222}
.foot-links span{padding:0 10px}
.copy{left:0;top:1180px;width:796px;text-align:center;font-size:8.3px;color:#666}
</style>
</head>
<body>

<header class="site-header">
  <div class="abs brand">ZYL PANDO</div>
  <div class="abs pill" style="left:584px;top:11px;width:52px">LOGIN</div>
  <div class="abs pill" style="left:643px;top:11px;width:51px">SING UP</div>
  <div class="abs phone">+44 (0)1632 960418</div>
</header>

<nav class="abs main-nav">
  <ul>
    <li class="active">HOME</li><li>ABOUT US</li><li>OUR BLOG</li><li>TESTIMONIALS</li><li>AFFILIATES</li><li>ADVERTISERS</li><li>CONTACT US</li>
  </ul>
</nav>

<section class="abs hero"></section>
<div class="abs map" role="img" aria-label="World map with orange location pins marking affiliate locations"></div>
<div class="abs laptop" role="img" aria-label="Laptop with banknotes flying out of the screen"></div>
<h1 class="abs hero-title">INTERNATIONAL<span>AFFILIATE NETWORK</span></h1>
<ul class="abs feature-list">
  <li><svg width="36" height="24" viewBox="0 0 36 24"><rect x="1" y="1" width="34" height="22" fill="none" stroke="#fff" stroke-width="2"/><rect x="5" y="5" width="26" height="14" fill="#fff" opacity=".5"/></svg>BANNER<br><span style="font-weight:400">FLASH - JPG - GIF</span></li>
  <li><svg width="36" height="32" viewBox="0 0 36 32"><rect x="6" y="1" width="24" height="30" rx="3" fill="none" stroke="#fff" stroke-width="2"/><circle cx="18" cy="27" r="1.5" fill="#fff"/></svg>MOBILE ADS</li>
  <li><svg width="36" height="22" viewBox="0 0 36 22"><rect x="1" y="1" width="30" height="20" fill="none" stroke="#fff" stroke-width="2"/><path d="M1 1 L16 13 L31 1" fill="none" stroke="#fff" stroke-width="2"/></svg>EMAIL<br>MARKETING</li>
  <li><svg width="36" height="26" viewBox="0 0 36 26"><rect x="1" y="1" width="32" height="24" fill="none" stroke="#fff" stroke-width="2"/><rect x="5" y="5" width="10" height="8" fill="#fff"/><path d="M18 6h11M18 10h11M5 16h24M5 20h24" stroke="#fff" stroke-width="2"/></svg>TEXT ADS</li>
  <li><svg width="30" height="30" viewBox="0 0 30 30"><rect x="3" y="5" width="10" height="18" rx="5" transform="rotate(-45 8 14)" fill="none" stroke="#fff" stroke-width="3"/><rect x="14" y="9" width="10" height="18" rx="5" transform="rotate(-45 19 18)" fill="none" stroke="#fff" stroke-width="3"/></svg>LINKS</li>
</ul>
<div class="abs join-btn">JOIN US TODAY!</div>
<div class="abs dots"><i></i><i></i><i></i></div>

<section class="abs intro"></section>
<div class="abs intro-hatch"></div>
<div class="abs intro-col" style="left:99px">
  <h2>AFFILIATES</h2>
  <p>Get access to a wide range of top performing offers for your websites and email marketing lists. Fresh and exclusive offers to promote. Join over 2,000 affiliates already signed up to Zyl Pando.</p>
</div>
<div class="abs cta" style="left:99px">SIGN UP NOW</div>
<div class="abs intro-col" style="left:410px">
  <h2>ADVERTISERS</h2>
  <p>Generate sales/leads to your website instantly with the Zyl Pando Affiliate Network. Only pay on performance, no monthly or setup fees. Zyl Pando takes the risk out of advertising.</p>
</div>
<div class="abs cta" style="left:410px">SIGN UP NOW</div>

<aside>
  <div class="abs login-box"></div>
  <div class="abs side-h" style="left:113px;top:610px">ACCOUNT LOGIN</div>
  <div class="abs field" style="top:637px">Email</div>
  <div class="abs field" style="top:675px">Password</div>
  <div class="abs small" style="left:113px;top:710px">Forgot Password</div>
  <div class="abs login-btn">LOGIN</div>
  <div class="abs small" style="left:160px;top:735px">or Sign Up</div>

  <div class="abs side-h" style="left:99px;top:784px">RECENT BLOG POSTS</div>
  <ul class="abs post-list">
    <li>New Offers For China</li><li>NEW: Banner Rotators</li><li>New Offers</li>
  </ul>
  <div class="abs rule" style="left:99px;width:142px;top:867px"></div>
  <div class="abs side-h" style="left:99px;top:883px">SOCIAL NETWORKING</div>
  <div class="abs social" style="left:101px;background:#3b5b98" role="img" aria-label="Social profile"></div>
  <div class="abs social" style="left:137px;background:#48b3e6" role="img" aria-label="Social profile"></div>
  <div class="abs social" style="left:174px;background:#c4282b" role="img" aria-label="Social profile"></div>
  <div class="abs social" style="left:211px;background:#1b7fb0" role="img" aria-label="Social profile"></div>
</aside>

<main>
  <h2 class="abs welcome-h">WELCOME TO ZYL PANDO</h2>
  <div class="abs welcome">
    <p>Welcome to the Zyl Pando affiliate network. On time payments, hot &amp; exclusive CPL/CPA offers, fast support and low fees for advertisers, is the making of a leading affiliate network!</p>
    <p>Zyl Pando offer a wide range of advertisers for your websites. So you can start monetizing your traffic or get an additional revenue stream, today.</p>
    <p>With the Zyl Pando Affiliate Network we focus on lead generation offers. We have a range of competitions, surveys, incentives and gambling offers. Whatever the industry, you will be able to find offers to suit your traffic.</p>
    <p>Zyl Pando is a powerful performance-based internet marketing network dedicated to advertisers to affiliates through its powerful affiliate network.</p>
  </div>

  <div class="abs why">
    <h3>WHY JOIN ZYL PANDO?</h3>
    <ul>
      <li>High Payouts</li><li>Reliable Tracking</li><li>Great Affiliate Support</li><li>Exclusive Offers</li>
      <li class="wrap">Monthly/Bi-monthly/Weekly Payments<br>&nbsp;&nbsp;(more info)</li>
      <li>View Stats on Your Mobile</li>
    </ul>
  </div>

  <h3 class="abs testi-h">TESTIMONIALS</h3>
  <p class="abs testi">"I decided to start using Zyl Pando after using several other networks. I was impressed with the customer service and support provided in comparison to some other networks I have used. Zyl Pando also has a large range of offers, retailers so is the perfect solution to earning commission. Payments are always on-time too."</p>
  <div class="abs testi-rule"></div>
  <div class="abs testi-by">Mara Ellison – Linkwell</div>

  <div class="abs rule" style="top:983px;width:250px"></div>
  <div class="abs rule" style="top:983px;left:447px;width:250px"></div>
  <h2 class="abs adv-h">ADVERTISERS</h2>
  <div class="abs adv-logo" style="left:103px"><i style="background:#7a1113"></i>Your Brand</div>
  <div class="abs adv-logo" style="left:203px"><i style="background:#d81f26;border-radius:50%"></i>SampleMark</div>
  <div class="abs adv-logo" style="left:280px"><i style="background:#7a1113"></i>Your Brand</div>
  <div class="abs adv-logo" style="left:368px"><i style="background:#d81f26;border-radius:50%"></i>SampleMark</div>
  <div class="abs adv-logo" style="left:450px"><i style="background:#7a1113"></i>Your Brand</div>
  <div class="abs adv-logo" style="left:544px"><i style="background:#d81f26;border-radius:50%"></i>SampleMark</div>
  <div class="abs adv-logo" style="left:630px"><i style="background:#7a1113"></i>Your Brand</div>
  <div class="abs rule" style="top:1083px"></div>

  <div class="abs badge" style="left:198px"><i style="background:#1b5d94"></i><span><b>Mobile Stats</b><s>Zyl Pando Mobile Website</s></span></div>
  <div class="abs badge" style="left:301px"><i style="background:#e66a1f;border-radius:50%"></i><span><b>Ember Browser</b><s>Official Zyl Pando Extension</s></span></div>
  <div class="abs badge" style="left:404px"><i style="background:#3a9a4a;border-radius:50%"></i><span><b>Prism Browser</b><s>Official Zyl Pando Extension</s></span></div>
  <div class="abs badge" style="left:508px"><i style="background:#8cbc2d"></i><span><b>Droidly App</b><s>Official Zyl Pando App</s></span></div>
</main>

<footer>
  <div class="abs site-footer"></div>
  <div class="abs footer-hatch"></div>
  <div class="abs foot-links">
    <span>Affiliate Terms &amp; Conditions</span><span>|</span><span>Advertiser Terms &amp; Conditions</span><span>|</span><span>Privacy Policy &amp; Cookies</span><span>|</span><span>FAQ</span><span>|</span><span>Contact Us</span>
  </div>
  <div class="abs copy">© 2013 Pando Media Ltd - All Rights Reserved.</div>
</footer>

</body>
</html>
```